IT services company requires Letterhead design

We need a professional letterhead designed to be used for general correspondence with customers, quotes, invoices etc. We are a new IT services company specialising in computer servicing and repairs and mobile and tablet repairs. Attached are templates that my printing company have supplied, my logos, an interpretation of our website for you to get a feel of the company. Details to be included on the letterhead are

Company Number – 4830517
VAT Number - 581736294
Registered Address – 14-16 Brambury Lane, London, E9 3PL

Phone – 01843 572236
Email – sales@quorvant.com
Web – www.quorvant.com

I would prefer for the top of the letterhead to just have the company logo on a white background and the rest of the details on the bottom of the letterhead but I am open to design ideas.

Thanks

```html
<!DOCTYPE html>
<html lang="en">
<head>
<meta charset="utf-8">
<title>Quorvant Letterhead</title>
<link href="https://fonts.googleapis.com/css2?family=Arimo:wght@400;700&family=Roboto:wght@300;400;700&display=swap" rel="stylesheet">
<style>
  :root {
    --backdrop: #e6e6e6;
    --paper: #ffffff;
    --charcoal: #45474c;
    --brand-dark: #3a3b3f;
    --brand-blue: #35c0e2;
    --ink: #141414;
    --muted: #444649;
    --signature-fill: #eceef3;
  }
  * { margin: 0; padding: 0; box-sizing: border-box; }
  html, body { width: 1200px; height: 1200px; overflow: hidden; }
  body { background: var(--backdrop); position: relative; }

  .letterhead {
    position: absolute; left: 182px; top: 60px;
    width: 836px; height: 1080px;
    background: var(--paper);
    font-family: "Arimo", Arial, sans-serif;
    color: var(--ink);
    overflow: hidden;
  }
  .header-wave { position: absolute; left: 0; top: 0; width: 836px; height: 110px; }

  .brand {
    position: absolute; left: 32px; top: 92px;
    display: flex; align-items: center; gap: 10px;
  }
  .brand-mark { width: 14px; height: 14px; background: var(--brand-blue); }
  .brand-name {
    font-family: "Roboto", Arial, sans-serif; font-weight: 700;
    font-size: 48px; letter-spacing: -0.5px; color: var(--brand-dark);
    line-height: 1;
  }

  .contact-list {
    position: absolute; right: 42px; top: 110px;
    list-style: none;
    font-family: "Roboto", sans-serif; font-weight: 300;
    font-size: 14px; color: #2d2e31; line-height: 19.5px;
  }
  .contact-list li { display: flex; align-items: center; gap: 5px; }
  .contact-list svg { width: 10px; height: 10px; fill: #3a3b3f; }

  .recipient { position: absolute; left: 41px; top: 231px; font-size: 15px; line-height: 24px; }

  .letter-body { position: absolute; left: 42px; top: 308px; width: 752px; font-size: 15px; line-height: 24px; }
  .letter-body p { margin-bottom: 25px; }

  .sign-off { position: absolute; left: 41px; top: 843px; font-size: 15px; line-height: 24px; }
  .signature {
    position: absolute; left: 58px; top: 872px; width: 96px; height: 58px;
    background: var(--signature-fill);
  }
  .signatory { position: absolute; left: 43px; top: 929px; font-size: 15px; font-weight: 700; line-height: 24px; }

  .company-details {
    position: absolute; left: 0; width: 100%; top: 1046px;
    text-align: center;
    font-family: "Roboto", sans-serif; font-weight: 400;
    font-size: 12px; color: var(--muted);
  }
  .company-details .divider { color: var(--brand-blue); margin: 0 6px; }
  .footer-band { position: absolute; left: 0; bottom: 0; width: 100%; height: 11px; background: var(--charcoal); }
</style>
</head>
<body>
  <main class="letterhead">
    <svg class="header-wave" viewBox="0 0 836 110" aria-hidden="true">
      <path d="M0,0 H836 V66 C700,92 560,88 420,56 C300,28 150,14 0,38 Z" fill="var(--charcoal)"/>
      <path d="M0,42 C150,20 300,34 420,62 C560,96 700,100 836,72 V80 C700,108 560,104 420,70 C300,44 150,34 0,60 Z" fill="var(--brand-blue)"/>
    </svg>

    <div class="brand">
      <span class="brand-mark"></span>
      <span class="brand-name">Quorvant</span>
    </div>

    <ul class="contact-list">
      <li><svg viewBox="0 0 10 10"><path d="M2,0.5 L3.8,2.6 L2.8,3.8 C3.5,5.3 4.7,6.5 6.2,7.2 L7.4,6.2 L9.5,8 L8.3,9.5 C4.3,9.2 0.8,5.7 0.5,1.7 Z"/></svg>01843 572236</li>
      <li><svg viewBox="0 0 10 10"><circle cx="5" cy="5" r="4.5" fill="none" stroke="#3a3b3f" stroke-width="1"/><path d="M0.5,5 H9.5 M5,0.5 V9.5" stroke="#3a3b3f" stroke-width="0.9"/><ellipse cx="5" cy="5" rx="2" ry="4.5" fill="none" stroke="#3a3b3f" stroke-width="0.9"/></svg>www.quorvant.com</li>
      <li><svg viewBox="0 0 10 10"><rect x="0.5" y="2" width="9" height="6.5"/><path d="M0.8,2.3 L5,5.6 L9.2,2.3" stroke="#fff" stroke-width="0.8" fill="none"/></svg>sales@quorvant.com</li>
    </ul>

    <div class="recipient">
      <div>Lorem Ipsum</div>
      <div>Lorem Ipsum Admin</div>
    </div>

    <section class="letter-body">
      <p>Lorem Ipsum is simply dummy text of the printing and typesetting industry. Lorem Ipsum has been the industry's standard dummy text ever since the 1500s, when an unknown printer took a galley of type and scrambled it to make a type specimen book. It has survived not only five centuries, but also the leap into electronic typesetting, remaining essentially unchanged.</p>
      <p>Lorem Ipsum is simply dummy text of the printing and typesetting industry. Lorem Ipsum has been the industry's standard dummy text ever since the 1500s, when an unknown printer took a galley of type and scrambled it to make a type specimen book.</p>
      <p>It has survived not only five centuries, but also the leap into electronic typesetting, remaining essentially unchanged. Lorem Ipsum is simply dummy text of the printing and typesetting industry. Lorem Ipsum has been the industry's standard dummy text ever since the 1500s, when an unknown printer took a galley of type and scrambled</p>
      <p>Lorem Ipsum is simply dummy text of the printing and typesetting industry. Lorem Ipsum has been the industry's standard dummy text ever since the 1500s, when an unknown printer took a galley of type and scrambled it to make a type specimen book. It has survived not only five centuries, but also the leap into electronic typesetting, remaining essentially unchanged.</p>
      <p>It was popularised in the 1960s with the release of Typemark sheets containing Lorem Ipsum passages, and more recently with desktop publishing software like Corvel PageSetter including versions of Lorem Ipsum.</p>
    </section>

    <div class="sign-off">Lorem Ipsum</div>
    <div class="signature" role="img" aria-label="Handwritten signature"></div>
    <div class="signatory">Lorem Ipsum Admin</div>

    <footer class="company-details">
      Company Number - 4830517<span class="divider">|</span>VAT Number - 581736294<span class="divider">|</span>Address - 14-16 Brambury Lane, London, E9 3PL
    </footer>
    <div class="footer-band"></div>
  </main>
</body>
</html>
```